Visually Compelling Flyer Design - Harbor Perks

We are a life insurance company looking to create visually compelling flyers that gain attention of potential buyers and simplify the concept. It should be professional, friendly, approachable in nature. Our logo and several rough drafts are included.
We are looking to refine this look and make it ultra professional, clean and easy to follow. A creative brief with brand guidelines is also included.
FLYER 1 — PAY YOURSELF FIRST
EYEBROW TAG
YOUR COMPANY JUST UPGRADED YOUR BENEFITS
HEADLINE
One small decision. A lifetime of protection.
SUBHEADLINE
Permanent life insurance + long-term care coverage, starting at $1 a day.
EYEBROW TAG
CHOOSE YOUR DAILY INVESTMENT
STAT — TIER 1
$1 / day → $20,000 Life Insurance
STAT — TIER 2 (HERO — make this one biggest/most prominent)
$2 / day → $40,000 Life Insurance
★ Most Popular
STAT — TIER 3
$3 / day → $60,000 Life Insurance
CAPTION
Rate locked at enrollment. Benefit never decreases.
EYEBROW TAG
THREE BENEFITS. ONE POLICY.
SUBHEADLINE
Your money works three ways.
CALLOUT — BENEFIT 1
01 | Cash Value Growth
BODY
Averages 6% annually over the last 50 years — guaranteed never to fall below 3%. Better than any savings account. And if you ever need it, you can borrow against it. It's your money.
CALLOUT — BENEFIT 2
02 | Tax-Free Death Benefit
BODY
From day one, your family is protected. The full benefit is paid tax-free to the person you choose — no waiting period, no exceptions. That's your legacy, preserved.
CALLOUT — BENEFIT 3
03 | Long-Term Care Coverage
BODY
70% of Americans will need long-term care. This plan pays 75% of your benefit — upfront and tax-free — to cover those costs while you're still alive. Your retirement savings stay intact. Your family stays protected.
EYEBROW TAG
ALREADY HAVE LIFE INSURANCE THROUGH WORK?
SUBHEADLINE
That's term. It ends when you need it most.
BODY
Term life insurance is designed for temporary needs — protecting your paycheck, your mortgage, your kids while they're home. When you retire, the house is paid off and your children are grown. Term ends because the need ends.
BODY
But one need never ends: your final expenses and the cost of long-term care. This permanent plan stays with you after retirement — when term coverage is gone and getting new coverage is expensive or impossible.
COMPARISON — LEFT COLUMN HEADER
✕ TERM LIFE
COMPARISON — LEFT COLUMN ITEMS
Gets more expensive with age
Ends at retirement
No cash value
Temporary protection only
COMPARISON — RIGHT COLUMN HEADER
✓ THIS PLAN
COMPARISON — RIGHT COLUMN ITEMS
Rate locked forever at enrollment
Stays with you after retirement
Builds real cash value
Permanent protection for life
EYEBROW TAG
WHAT MAKES THIS DIFFERENT
SUBHEADLINE
Built for you. Stays with you.
CALLOUT
✓ Guaranteed Issued
No medical exams. No questions asked. You qualify.
CALLOUT
✓ Group Rate
Because you work here, you get pricing individuals can't access on their own.
CALLOUT
✓ Rate Locked Forever
Your premium never increases. Your benefit never decreases.
CALLOUT
✓ Portable
Change jobs. Retire. Your policy comes with you at the same rate.
CALLOUT
✓ Family Coverage
Protect your spouse and children under the same plan.
SUBHEADLINE
Protect retirement. Preserve dignity. Plan ahead.
CTA
Be on the lookout for your personalized coverage details.
CAPTION
Brokered by Harbor Perks · Underwritten by TrueLedger
FLYER 2 — THE LONG-TERM CARE REALITY
EYEBROW TAG
WHAT MOST PEOPLE DON'T KNOW — BUT SHOULD
HEADLINE
Most Americans are unprepared. You don't have to be.
SUBHEADLINE
The long-term care gap is real — and it affects families like yours.
EYEBROW TAG
THE NUMBERS ARE HARD TO IGNORE
STAT
70%
of Americans age 65 and older will need some form of long-term care during their lifetime.
CAPTION
Source: Pryce & Lomax, Review of Elder Welfare and Civic Planning, 2018
STAT
3–4%
of Americans over 50 own a private long-term care insurance policy. The gap between who needs it and who has it is staggering.
CAPTION
Source: Stroud & Bellamy, QVT Wellness Wire, 2023
STAT
$700 Billion+
Estimated annual U.S. long-term care cost — and it's growing every year.
CAPTION
Source: Delacroix Wynn & Pasternak, Civic Ledger Council, 2020
STAT
$470 Billion
The estimated value of unpaid care provided by family members every year. That's the real cost — measured in time, stress, and financial sacrifice.
CAPTION
Source: Tillman & Osei, Meridian Bureau
STAT
80%
of total long-term care spending goes directly to assist retirees. This isn't a young person's problem. But the time to plan is now.
CAPTION
SUBHEADLINE
Long-term care doesn't just cost money. It costs families.
BODY
When there's no plan in place, the people you love absorb the impact — financially, emotionally, and physically. Retirement savings built over a lifetime can disappear in months. Family members step back from their own lives to provide care. Dignity becomes a daily negotiation.
BODY
This is not inevitable. A small decision today changes the entire outcome.
EYEBROW TAG
THE SOLUTION
HEADLINE
The Pay Yourself First Principle.
BODY
Take the first $1, $2, or $3 you make every day and invest it in a permanent life insurance policy that includes long-term care coverage — underwritten by TrueLedger, offered through your employer at a group rate, and Guaranteed Issued for everyone.
STAT
$1 / day → $20,000 $2 / day → $40,000 $3 / day → $60,000
BODY
The benefit includes three protections in one: a cash value that grows at an average of 6% annually, a tax-free death benefit for your family, and long-term care coverage that pays 75% of your benefit upfront — tax-free — when you need care most.
SUBHEADLINE
Whether you're single, married, with children or without — there is protection in this plan for you.
HEADLINE
CTA
Look for your personalized offer. Coverage details are coming your way.
CAPTION
COPY RULES FOR DESIGNERS
Headlines are one idea only. Never more than two lines.
Stats stand alone. Never buried in a paragraph.
Body copy maxes at 3 sentences per block. If it's longer, cut it.
The $2/day tier is always the hero. Always.
"Guaranteed Issued" appears on both flyers. It's the most important trust signal.
TrueLedger is always attributed. Always.
The tagline is: Protect retirement. Preserve dignity. Plan ahead. — Use it verbatim.
Target Market(s)
Average Americans with a family - adults looking for life insurance
Industry/Entity Type
Life Insurance & Financial Retirement

```html
<!DOCTYPE html>
<html lang="en">
<head>
<meta charset="utf-8">
<title>Harbor Perks – One Small Decision</title>
<link href="https://fonts.googleapis.com/css2?family=Montserrat:wght@400;600;700;800&family=Figtree:wght@400;500;600;700&display=swap" rel="stylesheet">
<style>
  :root{
    --navy:#0b4ea2;
    --blue:#0f74c4;
    --cyan:#0cb9e2;
    --ink:#1c2430;
    --muted:#4a5563;
    --tint:#eef8fc;
    --line:#a9d3ea;
    --white:#ffffff;
  }
  *{margin:0;padding:0;box-sizing:border-box}
  html,body{width:927px;height:1200px;overflow:hidden;background:var(--white)}
  body{font-family:"Figtree",sans-serif;color:var(--ink)}
  .flyer{position:relative;width:927px;height:1200px;overflow:hidden;background:var(--white)}
  .abs{position:absolute}

  .scene-photo{position:absolute;left:0;top:150px;width:927px;height:980px;
    background:linear-gradient(160deg,#f4f8fb 0%,#e3edf3 35%,#dbe6ec 55%,#eef3f6 80%,#f6f9fb 100%)}
  .header-curve,.footer-wave{position:absolute;left:0;width:927px}
  .header-curve{top:0;height:300px}
  .footer-wave{top:990px;height:210px}

  .brand{left:96px;top:60px;width:160px;text-align:center}
  .brand-dot{width:70px;height:70px;border-radius:50%;border:7px solid var(--cyan);margin:0 auto 12px}
  .brand-name{font-family:"Montserrat",sans-serif;font-weight:800;color:var(--navy);font-size:30px;line-height:1.02;letter-spacing:.5px}

  .eyebrow{left:320px;top:36px;font-size:13px;font-weight:500;letter-spacing:.3px;color:var(--ink)}
  .headline{left:319px;top:60px;font-family:"Montserrat",sans-serif;color:var(--navy);line-height:1}
  .headline .lead{display:block;font-weight:800;font-size:38px;letter-spacing:-.3px}
  .headline .follow{display:block;font-weight:400;font-size:37px;margin-top:12px;letter-spacing:.2px}
  .subhead{left:320px;top:166px;font-size:19px;color:var(--muted);letter-spacing:.3px}
  .subhead strong{display:block;color:var(--blue);font-weight:600;font-size:22px;margin-top:3px}

  .panel{position:absolute;background:rgba(255,255,255,.93);border:1.5px solid var(--line);border-radius:10px}
  .panel-tag{position:absolute;background:var(--blue);color:var(--white);border-radius:5px;
    font-family:"Montserrat",sans-serif;font-weight:400;font-size:20px;display:flex;align-items:center;justify-content:center;letter-spacing:.2px}

  .invest{left:32px;top:348px;width:466px;height:213px}
  .invest-tag{left:62px;top:324px;width:405px;height:41px}
  .tier{position:absolute;top:387px;width:131px;height:115px;border:1.5px solid var(--line);border-radius:9px;background:var(--tint);text-align:center;padding-top:17px}
  .tier-price{font-family:"Montserrat",sans-serif;font-weight:800;font-size:20px;color:var(--ink)}
  .tier-amount{font-weight:600;font-size:18px;color:var(--blue);margin-top:10px}
  .tier-label{font-size:13px;color:var(--ink);margin-top:7px}
  .tier-hero{border-color:var(--blue)}
  .tier-badge{position:absolute;left:50%;top:-9px;transform:translateX(-50%);background:var(--blue);color:var(--white);font-size:8px;font-weight:700;padding:3px 10px;border-radius:8px;white-space:nowrap}
  .invest-caption{left:32px;top:516px;width:466px;text-align:center;font-size:14.5px}

  .term-head{left:49px;top:590px;font-family:"Montserrat",sans-serif;color:var(--navy);line-height:1}
  .term-head b{display:block;font-weight:800;font-size:24px}
  .term-head span{display:block;font-weight:400;font-size:23px;margin-top:10px}
  .term-sub{left:49px;top:661px;font-weight:700;font-size:16px;color:var(--blue)}
  .term-body{left:49px;top:690px;width:425px;font-size:10.6px;line-height:17.5px;color:var(--ink)}
  .term-body .strong{font-weight:600}

  .compare{left:32px;top:809px;width:466px;height:170px;background:rgba(240,248,252,.95)}
  .compare-head{position:absolute;top:819px;width:213px;height:33px;border-radius:5px;color:var(--white);
    font-family:"Montserrat",sans-serif;font-weight:700;font-size:14px;display:flex;align-items:center;justify-content:center;gap:10px}
  .compare-head.cons{left:50px;background:var(--blue)}
  .compare-head.pros{left:270px;background:var(--cyan)}
  .compare-list{position:absolute;top:867px;list-style:none;font-size:11.5px;color:var(--muted)}
  .compare-list li{height:22px;display:flex;align-items:center;gap:9px}
  .compare-list.cons{left:49px}
  .compare-list.pros{left:269px}
  .mark{width:10px;height:10px;flex:none}

  .tagline{left:77px;top:1043px;font-family:"Montserrat",sans-serif;font-weight:800;color:var(--white);font-size:20px;line-height:29px;letter-spacing:.2px}
  .cta{left:78px;top:1109px;width:426px;height:30px;background:var(--white);border-radius:4px;color:var(--blue);
    font-family:"Montserrat",sans-serif;font-weight:700;font-size:10.5px;display:flex;align-items:center;justify-content:center;letter-spacing:.2px}
  .credit{left:77px;top:1150px;color:var(--white);font-size:12.5px}
  .page-code{right:12px;top:1187px;font-size:9px;color:var(--ink)}

  .benefits{left:516px;top:348px;width:378px;height:437px}
  .benefits-tag{left:537px;top:324px;width:337px;height:41px}
  .benefits-intro{left:516px;top:382px;width:378px;text-align:center;font-size:15px;color:var(--ink)}
  .benefit-icon{position:absolute;left:548px;width:54px;height:54px;border-radius:50%;display:flex;align-items:center;justify-content:center}
  .benefit-icon svg{width:24px;height:24px}
  .benefit{position:absolute;left:616px;width:245px}
  .benefit h3{font-size:15px;font-weight:700;color:var(--ink);margin-bottom:6px}
  .benefit p{font-size:10.7px;line-height:17.5px;color:var(--ink);text-align:justify}

  .different{left:516px;top:798px;width:378px;height:364px;background:rgba(238,247,252,.97)}
  .diff-head{left:565px;top:838px;font-family:"Montserrat",sans-serif;color:var(--navy);line-height:1}
  .diff-head b{display:block;font-weight:800;font-size:24px}
  .diff-head span{display:block;font-weight:400;font-size:24px;margin-top:10px}
  .diff-sub{left:565px;top:903px;font-weight:700;font-size:15.5px;color:var(--blue)}
  .feature{position:absolute;width:150px}
  .feature h4{display:flex;align-items:center;gap:8px;font-size:12.5px;font-weight:700;color:var(--ink);margin-bottom:6px}
  .feature p{font-size:10.8px;line-height:17.5px;color:var(--ink)}
</style>
</head>
<body>
<div class="flyer">

  <div class="scene-photo" role="img" aria-label="Soft-focus photo of a parent and child walking hand in hand on a sunny beach"></div>

  <svg class="header-curve" viewBox="0 0 927 300" preserveAspectRatio="none" aria-hidden="true">
    <defs>
      <linearGradient id="swoosh" x1="0" x2="1" y1="0" y2="0">
        <stop offset="0" stop-color="#0f74c4"/>
        <stop offset="1" stop-color="#0cc6e8"/>
      </linearGradient>
    </defs>
    <path d="M0 0 H927 V110 C760 230 560 275 420 270 C250 264 110 225 0 172 Z" fill="#ffffff"/>
    <path d="M0 172 C110 225 250 264 420 270 C560 275 760 230 927 110 L927 116 C760 244 560 292 420 292 C250 290 100 248 0 200 Z" fill="url(#swoosh)"/>
  </svg>

  <div class="abs brand">
    <div class="brand-dot"></div>
    <div class="brand-name">HARBOR<br>PERKS</div>
  </div>

  <p class="abs eyebrow">YOUR COMPANY JUST UPGRADED YOUR BENEFITS</p>
  <h1 class="abs headline"><span class="lead">ONE SMALL DECISION.</span><span class="follow">A LIFETIME OF PROTECTION.</span></h1>
  <p class="abs subhead">Permanent life insurance + long-term care coverage,<strong>Starting at $1 a day.</strong></p>

  <!-- Daily investment -->
  <div class="panel invest"></div>
  <div class="panel-tag invest-tag">CHOOSE YOUR DAILY INVESTMENT</div>
  <div class="tier" style="left:58px">
    <div class="tier-price">$1 / DAY</div>
    <div class="tier-amount">$20,000</div>
    <div class="tier-label">Life Insurance</div>
  </div>
  <div class="tier tier-hero" style="left:200px">
    <span class="tier-badge">MOST POPULAR</span>
    <div class="tier-price">$2 / DAY</div>
    <div class="tier-amount">$40,000</div>
    <div class="tier-label">Life Insurance</div>
  </div>
  <div class="tier" style="left:342px">
    <div class="tier-price">$3 / DAY</div>
    <div class="tier-amount">$60,000</div>
    <div class="tier-label">Life Insurance</div>
  </div>
  <p class="abs invest-caption">Rate locked at enrollment. Benefit never decreases.</p>

  <!-- Term comparison -->
  <h2 class="abs term-head"><b>ALREADY HAVE LIFE INSURANCE</b><span>THROUGH WORK?</span></h2>
  <p class="abs term-sub">That's term. It ends when you need it most.</p>
  <div class="abs term-body">
    <p class="strong">Term life insurance is designed for temporary needs — protecting your paycheck, your mortgage, your kids while they're home. When you retire, the house is paid off and your children are grown. Term ends because the need ends.</p>
    <p>But one need never ends: your final expenses and the cost of long-term care. This permanent plan stays with you after retirement — when term coverage is gone and getting new coverage is expensive or impossible.</p>
  </div>

  <div class="panel compare"></div>
  <div class="compare-head cons"><svg class="mark" viewBox="0 0 10 10"><path d="M1 1L9 9M9 1L1 9" stroke="#fff" stroke-width="1.8"/></svg>TERM LIFE</div>
  <div class="compare-head pros"><svg class="mark" viewBox="0 0 10 10"><path d="M1 1L9 9M9 1L1 9" stroke="#fff" stroke-width="1.8"/></svg>TERM LIFE</div>
  <ul class="compare-list cons">
    <li><svg class="mark" viewBox="0 0 10 10"><path d="M1 1L9 9M9 1L1 9" stroke="#0f74c4" stroke-width="1.6"/></svg>Gets more expensive with age</li>
    <li><svg class="mark" viewBox="0 0 10 10"><path d="M1 1L9 9M9 1L1 9" stroke="#0f74c4" stroke-width="1.6"/></svg>Ends at retirement</li>
    <li><svg class="mark" viewBox="0 0 10 10"><path d="M1 1L9 9M9 1L1 9" stroke="#0f74c4" stroke-width="1.6"/></svg>No cash value</li>
    <li><svg class="mark" viewBox="0 0 10 10"><path d="M1 1L9 9M9 1L1 9" stroke="#0f74c4" stroke-width="1.6"/></svg>Temporary protection only</li>
  </ul>
  <ul class="compare-list pros">
    <li><svg class="mark" viewBox="0 0 10 10"><path d="M1 5.5L4 8.5L9.5 2" fill="none" stroke="#0f74c4" stroke-width="1.6"/></svg>Rate locked forever at enrollment</li>
    <li><svg class="mark" viewBox="0 0 10 10"><path d="M1 5.5L4 8.5L9.5 2" fill="none" stroke="#0f74c4" stroke-width="1.6"/></svg>Stays with you after retirement</li>
    <li><svg class="mark" viewBox="0 0 10 10"><path d="M1 5.5L4 8.5L9.5 2" fill="none" stroke="#0f74c4" stroke-width="1.6"/></svg>Builds real cash value</li>
    <li><svg class="mark" viewBox="0 0 10 10"><path d="M1 5.5L4 8.5L9.5 2" fill="none" stroke="#0f74c4" stroke-width="1.6"/></svg>Permanent protection for life</li>
  </ul>

  <!-- Footer band -->
  <svg class="footer-wave" viewBox="0 0 927 210" preserveAspectRatio="none" aria-hidden="true">
    <defs>
      <linearGradient id="band" x1="0" x2="1" y1="0" y2="1">
        <stop offset="0" stop-color="#0f74c4"/>
        <stop offset="1" stop-color="#0cc6e8"/>
      </linearGradient>
    </defs>
    <path d="M0 52 C150 20 330 2 520 8 C700 14 830 70 927 140 V210 H0 Z" fill="url(#band)"/>
  </svg>
  <p class="abs tagline">PROTECT RETIREMENT.<br>PRESERVE DIGNITY. PLAN AHEAD.</p>
  <div class="abs cta">BE ON THE LOOKOUT FOR YOUR PERSONALIZED COVERAGE DETAILS.</div>
  <p class="abs credit">Brokered by Harbor Perks · Underwritten by TrueLedger</p>

  <!-- Three benefits -->
  <div class="panel benefits"></div>
  <div class="panel-tag benefits-tag">THREE BENEFITS. ONE POLICY.</div>
  <p class="abs benefits-intro">Your money works three ways.</p>

  <div class="benefit-icon" style="top:424px;background:var(--blue)">
    <svg viewBox="0 0 24 24"><path d="M3 12V4h8l10 10-7 7Z" fill="#fff"/><circle cx="7.5" cy="8" r="1.6" fill="#0f74c4"/></svg>
  </div>
  <div class="benefit" style="top:422px">
    <h3>Cash Value Growth</h3>
    <p>Averages 6% annually over the last 50 years — guaranteed never to fall below 3%. Better than any savings account. And if you ever need it, you can borrow against it. It's your money.</p>
  </div>

  <div class="benefit-icon" style="top:537px;background:var(--cyan)">
    <svg viewBox="0 0 24 24"><rect x="5" y="2" width="14" height="20" rx="2" fill="#fff"/><rect x="7.5" y="4.5" width="9" height="4" fill="#0cb9e2"/><g fill="#0cb9e2"><rect x="7.5" y="11" width="2.4" height="2.2"/><rect x="10.8" y="11" width="2.4" height="2.2"/><rect x="14.1" y="11" width="2.4" height="2.2"/><rect x="7.5" y="14.5" width="2.4" height="2.2"/><rect x="10.8" y="14.5" width="2.4" height="2.2"/><rect x="14.1" y="14.5" width="2.4" height="2.2"/><rect x="7.5" y="18" width="2.4" height="2.2"/><rect x="10.8" y="18" width="2.4" height="2.2"/><rect x="14.1" y="18" width="2.4" height="2.2"/></g></svg>
  </div>
  <div class="benefit" style="top:535px">
    <h3>Tax-Free Death Benefit</h3>
    <p>From day one, your family is protected. The full benefit is paid tax-free to the person you choose — no waiting period, no exceptions. That's your legacy, preserved.</p>
  </div>

  <div class="benefit-icon" style="top:650px;background:var(--blue)">
    <svg viewBox="0 0 24 24"><circle cx="12" cy="12" r="10" fill="#fff"/><path d="M12 6.5V12l3.5 2.5" fill="none" stroke="#0f74c4" stroke-width="2" stroke-linecap="round"/></svg>
  </div>
  <div class="benefit" style="top:648px">
    <h3>Long-Term Care Coverage</h3>
    <p>70% of Americans will need long-term care. This plan pays 75% of your benefit — upfront and tax-free — to cover those costs while you're still alive. Your retirement savings stay intact. Your family stays protected.</p>
  </div>

  <!-- What makes this different -->
  <div class="panel different"></div>
  <h2 class="abs diff-head"><b>WHAT MAKES THIS</b><span>DIFFERENT</span></h2>
  <p class="abs diff-sub">Built for you. Stays with you.</p>

  <div class="feature" style="left:565px;top:943px">
    <h4><svg class="mark" viewBox="0 0 10 10"><path d="M1 5.5L4 8.5L9.5 2" fill="none" stroke="#0f74c4" stroke-width="1.6"/></svg>Guaranteed Issued</h4>
    <p>No medical exams. No questions asked. You qualify.</p>
  </div>
  <div class="feature" style="left:565px;top:1010px;width:165px">
    <h4><svg class="mark" viewBox="0 0 10 10"><path d="M1 5.5L4 8.5L9.5 2" fill="none" stroke="#0f74c4" stroke-width="1.6"/></svg>Rate Locked Forever</h4>
    <p>Your premium never increases. Your benefit never decreases.</p>
  </div>
  <div class="feature" style="left:565px;top:1075px">
    <h4><svg class="mark" viewBox="0 0 10 10"><path d="M1 5.5L4 8.5L9.5 2" fill="none" stroke="#0f74c4" stroke-width="1.6"/></svg>Family Coverage</h4>
    <p>Protect your spouse and children under the same plan.</p>
  </div>
  <div class="feature" style="left:741px;top:943px;width:140px">
    <h4><svg class="mark" viewBox="0 0 10 10"><path d="M1 5.5L4 8.5L9.5 2" fill="none" stroke="#0f74c4" stroke-width="1.6"/></svg>Group Rate</h4>
    <p>Because you work here, you get pricing individuals can't access on their own.</p>
  </div>
  <div class="feature" style="left:741px;top:1025px;width:140px">
    <h4><svg class="mark" viewBox="0 0 10 10"><path d="M1 5.5L4 8.5L9.5 2" fill="none" stroke="#0f74c4" stroke-width="1.6"/></svg>Portable</h4>
    <p>Change jobs. Retire. Your policy comes with you at the same rate.</p>
  </div>

  <p class="abs page-code">C9</p>
</div>
</body>
</html>
```